Luxury Lifestyle Website - Blog and Product Showcasing

I am looking to create a simple, yet elegant website where I can post blog posts and feature products and brand partnerships for my company, Velmora Haus. I want a very elegant but not overly complex site. I like the look and feel of Corinne Ashdale's site - I don't need for it to be that robust or sophisticated, but that is the aesthetic I am going for. I would like to include my primary logo at the top of the main page, and also incorporate my alternative logos throughout the site in strategic places.

Target Market(s)

Luxury Brands; 20s-60s year olds; women; high-end fashion and tastes

Industry/Entity Type

Luxury Lifestyle - Blogging - Product Showcasing

Coding

Coded - Design and coding required

Number of Pages Required

4 page

Font styles to use
Sans Serif
Script
Other font styles liked:
• Pinyon

Colors
00AB8E
00BBA5
67D7C9
C6EFE9
E9F9F6
59FF00
82FF00
B8FF75
E3FFCB
F4FFEA

Requirements
Must have
• Creative use of my various logos. PASTEL GREENS or a DEEP DARK GREEN. Nothing bright, very soft and elegant.
Nice to have
• Elegant script that is easy to read.
Should not have
• Bright colors or overly modern look or feel.

```html
<!DOCTYPE html>
<html lang="en">
<head>
<meta charset="utf-8">
<title>Velmora Haus — Luxury Lifestyle</title>
<link rel="stylesheet" href="https://fonts.googleapis.com/css2?family=Yellowtail&family=Pinyon+Script&family=Work+Sans:ital,wght@0,400;0,500;0,600;1,400&display=swap">
<style>
:root{
  --paper:#f7f5f0;
  --teal:#00a98b;
  --teal-soft:#2bb89f;
  --mint:#67d7c9;
  --ink:#2e2e2e;
  --muted:#555;
  --rule:#dcdad4;
  --white:#ffffff;
}
*{box-sizing:border-box;margin:0;padding:0}
html,body{width:1200px;height:5381px;overflow:hidden}
body{background:var(--paper);color:var(--ink);font-family:"Work Sans",Arial,sans-serif;position:relative}
.abs{position:absolute}
.script{font-family:"Yellowtail",cursive;font-weight:400}
.link{font-size:10px;letter-spacing:2px;text-transform:uppercase;text-decoration:underline;text-underline-offset:3px;color:var(--ink)}
.link.teal{color:var(--teal)}
.center{text-align:center}
.photo{position:absolute}
.para{font-size:12.5px;line-height:27px;font-style:italic;color:var(--muted)}

/* header */
.site-header{top:0;left:0;width:1200px;height:100px}
.menu{left:115px;top:31px;display:flex;align-items:center;gap:12px;font-size:11px;letter-spacing:1px}
.menu svg{display:block}
.brand{left:0;width:1200px;top:10px;text-align:center}
.brand-name{font-family:"Pinyon Script",cursive;font-size:40px;color:var(--ink);line-height:50px}
.brand-tag{font-size:7px;letter-spacing:6px;color:var(--muted);text-transform:uppercase}
.utility{right:115px;top:31px;font-size:11px;letter-spacing:1px;display:flex;gap:14px}

/* hero */
.hero{top:100px;left:0;width:1200px;height:592px;background:linear-gradient(100deg,#2f3a2c 0%,#1e5e78 35%,#25324a 60%,#2d3b33 100%)}
.hero-title{left:600px;width:510px;top:262px;color:var(--white);font-size:46px;line-height:60px;text-align:center}
.hero-link{left:600px;width:510px;top:475px;text-align:center;color:var(--white)}

/* featured bars */
.feature-bar{left:115px;width:970px;display:flex;justify-content:space-between}
.rule{left:0;width:1200px;height:1px;background:var(--rule)}

/* cards */
.card-label{width:285px;text-align:center;font-size:11px;letter-spacing:2px;text-transform:uppercase}
.card-link{width:285px;text-align:center}

/* section headings */
.section-title{color:var(--teal);font-size:32px;line-height:48px}

/* shop */
.shop-band{top:2648px;left:0;width:1200px;height:560px;background:var(--teal)}
.shop-frame{left:113px;top:2765px;width:244px;height:332px;border:6px solid var(--white)}
.shop-btn{left:148px;top:2907px;width:172px;height:40px;background:var(--white);font-size:9px;letter-spacing:1px;text-decoration:underline;color:var(--teal);display:flex;align-items:center;justify-content:center}

/* product side */
.product-name{color:var(--teal);font-size:11px;font-style:italic;font-weight:500;letter-spacing:1px}
.product-text{font-size:12.5px;line-height:18px;font-style:italic;color:var(--muted);margin:8px 0 14px}

/* footer */
.site-footer{top:4946px;left:0;width:1200px;height:435px;background:var(--teal-soft);color:var(--white)}
.foot-col h4{font-size:11px;font-weight:600;letter-spacing:1px;margin-bottom:16px}
.foot-col li{list-style:none;font-size:10px;line-height:22px}
.field{border-bottom:1px solid rgba(255,255,255,.8);font-size:9px;padding-bottom:6px;margin-top:6px;width:205px;letter-spacing:1px}
</style>
</head>
<body>

<header class="abs site-header">
  <div class="abs menu">
    <svg width="26" height="16" viewBox="0 0 26 16"><path d="M0 1h26M0 8h26M0 15h26" stroke="#2e2e2e" stroke-width="2"/></svg>
    MENU
  </div>
  <div class="abs brand">
    <div class="brand-name">Velmora Haus</div>
    <div class="brand-tag">Luxury Lifestyle</div>
  </div>
  <div class="abs utility"><span>SEARCH</span><span>SHOP</span></div>
</header>

<section>
  <div class="photo hero" role="img" aria-label="Woman in a flowing blue dress in a garden beside a pool"></div>
  <h1 class="abs script hero-title">The Authority on Living an Elegantly Extravagant Existence</h1>
  <div class="abs hero-link"><span class="link" style="color:#fff">Read More</span></div>
</section>

<div class="abs feature-bar" style="top:740px"><span class="link">Featured Post</span><span class="link">Read All Posts</span></div>
<div class="abs rule" style="top:770px"></div>

<section>
  <div class="abs card-label" style="left:113px;top:840px">In the Dressing Room</div>
  <div class="abs card-label" style="left:465px;top:840px">In the Home &amp; Garden</div>
  <div class="abs card-label" style="left:803px;top:840px">Lifestyle</div>
  <div class="photo" role="img" aria-label="Floral slip dress on a hanger over a teal panel" style="left:113px;top:872px;width:285px;height:348px;background:linear-gradient(135deg,#5a6e58,#07a88d 40%,#09a88b 70%,#6b7060)"></div>
  <div class="photo" role="img" aria-label="Woman on a terrace overlooking a coastal town at dusk" style="left:465px;top:872px;width:285px;height:348px;background:linear-gradient(180deg,#8da6c2,#5d7286 45%,#3f4a4f)"></div>
  <div class="photo" role="img" aria-label="Woman in a jumpsuit on a terrace above the sea" style="left:803px;top:872px;width:285px;height:348px;background:linear-gradient(180deg,#4f7fbf,#9bbbe0 45%,#3a6fa0 62%,#d8d8d8)"></div>
  <div class="abs card-link" style="left:113px;top:1245px"><span class="link">Read More</span></div>
  <div class="abs card-link" style="left:465px;top:1245px"><span class="link">Read More</span></div>
  <div class="abs card-link" style="left:803px;top:1245px"><span class="link">Read More</span></div>
</section>

<div class="abs feature-bar" style="top:1298px"><span class="link">Featured Post</span><span class="link">Read All Posts</span></div>
<div class="abs rule" style="top:1325px"></div>

<section>
  <h2 class="abs script section-title center" style="left:0;width:1200px;top:1425px">More recently with desktop publishing software like Quillon</h2>
  <p class="abs para center" style="left:320px;width:560px;top:1490px;line-height:23px;font-size:12px">with the release of Typeline sheets containing Lorem Ipsum passages, and more recently with desktop publishing software like Quillon PageCraft including versions of Lorem Ipsum.</p>
  <div class="abs center" style="left:0;width:1200px;top:1606px"><span class="link teal">Read More</span></div>
</section>

<section>
  <div class="photo" role="img" aria-label="Woman in a red dress holding a glass of wine beside flowers" style="left:0;top:1714px;width:590px;height:482px;background:linear-gradient(100deg,#3b2620,#b23a24 30%,#d9cbbd 60%,#efe9e2)"></div>
  <div class="abs" style="left:510px;top:1678px;width:126px;height:126px;border-radius:50%;background:var(--paper);border:1px solid var(--rule)"></div>
  <div class="abs" style="left:525px;top:1693px;width:96px;height:96px;border-radius:50%;border:1px solid #8a8a8a"></div>
  <h2 class="abs script section-title center" style="left:640px;width:470px;top:1790px;line-height:46px">With the release of Typeline sheets containing Lorem Ipsum passages,</h2>
  <p class="abs para center" style="left:655px;width:420px;top:1903px">Lorem Ipsum is simply dummy text of the printing and typesetting industry. Lorem Ipsum has been the industry's standard dummy text ever since the 1500s, when an unknown printer took a galley of type and scrambled it to make a type specimen book. It has survived not only five centuries, but also the leap into electronic</p>
  <div class="abs center" style="left:650px;width:450px;top:2105px"><span class="link teal">Read More</span></div>
</section>

<div class="abs rule" style="top:2222px"></div>
<div class="abs feature-bar" style="top:2243px"><span class="link">Featured Post</span><span class="link">Read All Posts</span></div>
<div class="abs rule" style="top:2270px"></div>

<section>
  <h2 class="abs script section-title center" style="left:0;width:1200px;top:2370px">With the release of Typeline sheets containing Lorem Ipsum passages,</h2>
  <p class="abs para center" style="left:0;width:1200px;top:2428px;line-height:31px;font-size:12px">Lorem Ipsum is simply dummy text of the printing and typesetting industry.<br>Lorem Ipsum has been the industry's standard dummy te</p>
  <div class="abs center" style="left:0;width:1200px;top:2538px"><span class="link teal">Read More</span></div>
</section>

<section>
  <div class="abs shop-band"></div>
  <h2 class="abs script center" style="left:0;width:1200px;top:2690px;color:#fff;font-size:34px">My Shop</h2>
  <div class="abs shop-frame"></div>
  <div class="photo" role="img" aria-label="Navy lace dress on a hanger" style="left:140px;top:2800px;width:190px;height:250px;background:linear-gradient(180deg,#2f3d78,#3c4c90);border-radius:40px 40px 8px 8px"></div>
  <div class="abs shop-btn">SHOP NOW &nbsp;→</div>
  <div class="photo" role="img" aria-label="Leopard print blouse on a hanger" style="left:430px;top:2800px;width:180px;height:240px;background:linear-gradient(180deg,#e8dccb,#7a6a5a);border-radius:40px 40px 10px 10px"></div>
  <div class="photo" role="img" aria-label="Floral slip dress on a hanger" style="left:690px;top:2790px;width:100px;height:265px;background:linear-gradient(180deg,#2a3550,#3d4a6a);border-radius:20px 20px 10px 10px"></div>
  <div class="photo" role="img" aria-label="Multicoloured print shirt on a hanger" style="left:875px;top:2790px;width:170px;height:250px;background:linear-gradient(160deg,#c2442a,#d5a53a 40%,#356a4a 70%,#2b2b2b);border-radius:40px 40px 10px 10px"></div>
  <div class="abs center" style="left:0;width:1200px;top:3146px"><span class="link" style="color:#fff">Visit My Shop</span></div>
</section>

<div class="abs rule" style="top:3218px"></div>
<div class="abs feature-bar" style="top:3249px"><span class="link">Featured Post</span><span class="link">Read All Posts</span></div>
<div class="abs rule" style="top:3276px"></div>

<section>
  <h2 class="abs script" style="left:115px;top:3342px;width:460px;font-size:32px;line-height:46px;color:var(--ink)">Latin professor at Ashford-Lyle College in Virginia, looked up one</h2>
  <p class="abs para" style="left:115px;width:385px;top:3448px">Lorem Ipsum is simply dummy text of the printing and typesetting industry. Lorem Ipsum has been the industry's standard dummy text ever since the 1500s, when an unknown printer took a galley of type and scrambled it to make a type specimen book. It has survived not only five centuries, but also the leap into electronic</p>
  <div class="abs" style="left:115px;top:3690px"><span class="link teal">Visit My Shop</span></div>
  <svg class="abs" style="left:115px;top:3735px" width="110" height="36" viewBox="0 0 110 36"><path d="M2 18h38M2 18l8-6M2 18l8 6" stroke="#00a98b" stroke-width="1.6" fill="none"/><path d="M46 34l12-32" stroke="#2e2e2e" stroke-width="1.2"/><path d="M66 18h40M106 18l-8-6M106 18l-8 6" stroke="#2e2e2e" stroke-width="1.6" fill="none"/></svg>

  <div class="abs" style="left:688px;top:3355px;width:190px">
    <div class="product-name">Lunessa Riviera Shirt</div>
    <p class="product-text">Lorem Ipsum is simply dummy text of the printing and typesetting.</p>
    <span class="link teal">Read More</span>
  </div>
  <div class="photo" role="img" aria-label="Pink knit sweater on a hanger" style="left:905px;top:3325px;width:140px;height:190px;background:linear-gradient(180deg,#e4b2bc,#cf95a2);border-radius:30px 30px 8px 8px"></div>
  <div class="photo" role="img" aria-label="Patterned knit sweater on a hanger" style="left:695px;top:3560px;width:125px;height:220px;background:linear-gradient(180deg,#8b6f66,#c9a79a 60%,#ece3dc);border-radius:30px 30px 8px 8px"></div>
  <div class="abs" style="left:872px;top:3592px;width:200px">
    <div class="product-name">Lunessa Riviera Shirt</div>
    <p class="product-text">Lorem Ipsum is simply dummy text of the printing and typesetting</p>
    <span class="link teal">Read More</span>
  </div>
</section>

<section>
  <h2 class="abs script center" style="left:0;width:1200px;top:3845px;font-size:34px;color:var(--ink)">Recent Videos</h2>
  <div class="photo" role="img" aria-label="Video still of a woman in a blue dress, teal tinted" style="left:0;top:3925px;width:330px;height:395px;background:linear-gradient(180deg,#2a9c8c,#0ea58a)"></div>
  <div class="photo" role="img" aria-label="Video still of a woman in a black dress in a mirrored bar" style="left:330px;top:3925px;width:558px;height:395px;background:linear-gradient(100deg,#3a2c22,#8a6a4e 45%,#2b2420 70%,#6a5240)"></div>
  <div class="photo" role="img" aria-label="Video still of a woman on a velvet sofa, teal tinted" style="left:888px;top:3925px;width:312px;height:395px;background:linear-gradient(180deg,#2cae97,#1aa68e)"></div>
  <svg class="abs" style="left:582px;top:4097px" width="50" height="50" viewBox="0 0 50 50"><circle cx="25" cy="25" r="24" fill="#fff"/><path d="M20 15l14 10-14 10z" fill="#2e2e2e"/></svg>
  <svg class="abs" style="left:25px;top:4115px" width="45" height="20" viewBox="0 0 45 20"><path d="M2 10h40M2 10l8-6M2 10l8 6" stroke="#fff" stroke-width="1.8" fill="none"/></svg>
  <svg class="abs" style="left:1130px;top:4115px" width="45" height="20" viewBox="0 0 45 20"><path d="M3 10h40M43 10l-8-6M43 10l-8 6" stroke="#fff" stroke-width="1.8" fill="none"/></svg>

  <div class="abs" style="left:183px;top:4350px;font-size:10px;text-decoration:underline">‹ Prev</div>
  <div class="abs center para" style="left:0;width:1200px;top:4343px;font-size:11.5px">Simply dummy text of the printing and typesetting industry.</div>
  <div class="abs" style="left:975px;top:4350px;font-size:10px;text-decoration:underline">Next ›</div>
  <div class="abs" style="left:115px;top:4393px;width:970px;height:1px;background:var(--rule)"></div>
</section>

<section>
  <h2 class="abs script center" style="left:0;width:1200px;top:4475px;font-size:32px;color:var(--ink)">And more recently with desktop publishing software like Quillon PageCraft</h2>
  <p class="abs para center" style="left:0;width:1200px;top:4530px;font-size:11.5px">Simply dummy text of the printing and typesetting industry.</p>
  <div class="abs center" style="left:0;width:1200px;top:4604px"><span class="link teal">Read More</span></div>
  <h2 class="abs script center" style="left:0;width:1200px;top:4672px;font-size:32px;color:var(--ink)">Follow us on Snapfolio</h2>
  <div class="photo" role="img" aria-label="Woman in red beside flowers" style="left:113px;top:4735px;width:150px;height:120px;background:linear-gradient(120deg,#5a2a22,#b8432b,#e6ddd2)"></div>
  <div class="photo" role="img" aria-label="Woman on a velvet sofa" style="left:277px;top:4735px;width:150px;height:120px;background:linear-gradient(180deg,#e9e1d4,#a06a3c)"></div>
  <div class="photo" role="img" aria-label="Woman on a terrace above the sea" style="left:441px;top:4735px;width:150px;height:120px;background:linear-gradient(180deg,#5d8fc8,#9cc0e4 55%,#ccc)"></div>
  <div class="photo" role="img" aria-label="Woman overlooking a coastal town" style="left:605px;top:4735px;width:150px;height:120px;background:linear-gradient(180deg,#3f6aa8,#5e6f80,#3b3b3e)"></div>
  <div class="photo" role="img" aria-label="Woman on a poolside lounger" style="left:770px;top:4735px;width:150px;height:120px;background:linear-gradient(160deg,#4e7a4a,#5fb7b0,#c9b88f)"></div>
  <div class="photo" role="img" aria-label="Woman seated by a seaside pool" style="left:935px;top:4735px;width:150px;height:120px;background:linear-gradient(180deg,#7aa2d4,#dfe7ee 55%,#3a5f8a)"></div>
</section>

<footer class="abs site-footer">
  <div class="abs" style="left:113px;top:105px;width:60px;height:60px;border:1.5px solid #fff"></div>
  <div class="abs" style="left:113px;top:180px;font-size:20px;letter-spacing:1px">VELMORA HAUS</div>
  <div class="abs" style="left:113px;top:208px;font-size:7px;letter-spacing:5px">LUXURY LIFESTYLE</div>

  <div class="abs foot-col" style="left:440px;top:100px"><h4>ABOUT</h4><ul><li>Corinne Ashdale</li><li>FAQ</li><li>Contact</li><li>Shop</li><li>Privacy Policy</li></ul></div>
  <div class="abs foot-col" style="left:597px;top:96px"><h4>TOPICS</h4><ul><li>Corinne Ashdale</li><li>FAQ</li><li>Contact</li><li>Shop</li><li>Privacy Policy</li></ul></div>
  <div class="abs foot-col" style="left:738px;top:100px"><h4>SOCIAL</h4><ul><li>Snapfolio</li><li>Reelcast</li><li>Pinvault</li><li>Clipwave</li></ul></div>
  <div class="abs foot-col" style="left:870px;top:96px">
    <h4>NEWSLETTER SUBSCRIBE</h4>
    <div style="font-size:9px;letter-spacing:.5px">GET UPDATES &amp; EXCLUSIVE NEWS</div>
    <div class="field">First Name</div>
    <div class="field" style="margin-top:30px">Email Address</div>
    <div style="font-size:9px;text-decoration:underline;margin-top:16px;letter-spacing:1px">Subscribe Now</div>
  </div>
  <svg class="abs" style="left:1032px;top:272px" width="36" height="36" viewBox="0 0 36 36"><circle cx="18" cy="18" r="17" fill="#00a98b" stroke="#fff" stroke-opacity=".4"/><path d="M12 21l6-6 6 6" stroke="#fff" stroke-width="1.6" fill="none"/></svg>
  <div class="abs center" style="left:0;width:1200px;top:352px;font-size:10px;font-weight:600">Copyright © 2023 Velmora Haus</div>
</footer>

</body>
</html>
```